Office Stationary and Business Card package

I need a new fresh looking business card and stationary design. "I need to refresh and update my Stationary and Business card appearance.

We are a family dental practice that handles all phases of dentistry including cosmetic, emergency and implant restoration We like the use of Blue and Grey in the design. i would like to include my website address and Phone numbers on the new project as well as a choice of different back sides to business cards which might include a map, appointment information, or blank depending on the particular card. The business cards should allow for the inclusion of another persons name and title in some location.

Information to be included in stationery:

Gordon T Vallow DMD, FAIDS
A Professional Dental Corporation (this needs to be
somewhere on the stationary and business cards)
48610 Marlow Avenue
Larkdale, CA 90712
PHONE: (562) 471-3095
WEBSITE: www.gordonvallowdmd-example.com

Designs need to be Vibrant, Professional and Clean.
Colors to use: Blue, Grey and White colors.

I currently do not have an existing logo. I would like something simply, similar to the attached.

```html
<!DOCTYPE html>
<html lang="en">
<head>
<meta charset="utf-8">
<title>Marlow Dental – Stationery Set</title>
<link rel="stylesheet" href="https://fonts.googleapis.com/css2?family=Arimo:wght@400;700&family=Tinos:ital@1&display=swap">
<style>
:root{
  --blue:#2a8fc9;
  --blue-light:#39b0e0;
  --blue-dark:#1b73b3;
  --charcoal:#4a4646;
  --ink:#222;
  --grey:#7a7a7a;
  --paper:#fff;
  --stage:#e4e4e4;
}
*{box-sizing:border-box;margin:0;padding:0}
html,body{width:1200px;height:1000px;overflow:hidden}
body{background:radial-gradient(ellipse at 50% 40%,#f2f2f2 0%,var(--stage) 75%);font-family:"Arimo",Arial,sans-serif;color:var(--ink);position:relative}
.sheet{position:absolute;background:var(--paper);box-shadow:0 1px 4px rgba(0,0,0,.18)}
.brand{position:absolute;display:flex;align-items:center;gap:6px}
.brand-dot{width:var(--d,24px);height:var(--d,24px);border-radius:50%;background:var(--blue);flex:none}
.brand-name{font-family:"Arimo",Arial,sans-serif;font-weight:400;color:var(--blue);white-space:nowrap}
.tagline{position:absolute;font-size:5px;letter-spacing:.2px;color:var(--grey);text-transform:uppercase;white-space:nowrap}
.corp{position:absolute;font-size:7px;color:var(--grey);white-space:nowrap}
.band-line{position:absolute;left:0;right:0;background:var(--blue);height:3px}
.band{position:absolute;left:0;right:0;background:var(--charcoal);color:#fff}

/* Letterhead */
.letterhead{left:47px;top:139px;width:516px;height:731px}
.letterhead .recipient{position:absolute;left:45px;top:172px;font-size:9.5px;line-height:13.5px}
.letterhead .body{position:absolute;left:45px;top:252px;width:428px;font-size:9.2px;line-height:13px;text-align:justify}
.letterhead .body p{margin-bottom:13px}
.signature{position:absolute;left:45px;top:588px;width:125px;height:34px;background:linear-gradient(90deg,#3b3b3b22,#3b3b3b10)}
.signer{position:absolute;left:45px;top:627px;font-size:9px;color:var(--blue)}
.letterhead .band-line{top:704px}
.letterhead .band{top:707px;height:24px;display:flex;justify-content:center;align-items:center;gap:18px;font-size:7.5px;white-space:nowrap}
.contact{display:flex;align-items:center;gap:4px;white-space:nowrap}
.contact svg{width:8px;height:8px;fill:var(--blue-light);flex:none}

/* Envelope */
.env-front{left:597px;top:139px;width:564px;height:255px}
.sender{position:absolute;left:29px;top:87px}
.sender .name{font-size:9.5px;color:var(--blue);margin-bottom:4px}
.sender .rows{display:flex;font-size:6.8px;color:#555;line-height:10.5px;white-space:nowrap}
.sender .col{padding-right:12px}
.sender .col+.col{border-left:1px solid #999;padding-left:12px}
.window{position:absolute;left:30px;top:134px;width:186px;height:70px;border-radius:3px;background:linear-gradient(160deg,#e8e8e8,#cfcfcf 50%,#e2e2e2);border:1px solid #d8d8d8}
.env-front .band-line{top:234px}
.env-front .band{top:237px;height:18px}
.env-back{left:597px;top:413px;width:564px;height:255px}
.flap{position:absolute;left:0;top:0;width:564px;height:76px}
.env-back .web{position:absolute;left:0;right:0;top:229px;text-align:center;font-size:10px;color:var(--blue-dark)}

/* Business cards */
.card-front{left:597px;top:700px;width:276px;height:166px;overflow:hidden}
.card-front .band-line{top:82px}
.card-front .band{top:85px;bottom:0;font-size:7px;line-height:10px;white-space:nowrap}
.card-front .notch{position:absolute;left:236px;top:84px;width:0;height:0;border-left:8px solid transparent;border-right:8px solid transparent;border-top:8px solid var(--blue)}
.card-front .addr{position:absolute;left:16px;top:12px}
.card-front .lines{position:absolute;left:16px;top:39px}
.card-front .lines b{color:var(--blue-light);font-weight:400}
.card-front .who{position:absolute;right:15px;top:12px;font-size:9px;color:var(--blue-light)}
.card-back{left:886px;top:700px;width:277px;height:166px;background:var(--charcoal)}
.card-back .form{position:absolute;left:15px;top:50px;width:243px;height:91px;background:#fff;font-size:8px}
.field{position:absolute;display:flex;align-items:flex-end;gap:3px;white-space:nowrap}
.field i{display:block;border-bottom:1px solid #aaa;height:1px;margin-bottom:2px}
.days{position:absolute;left:14px;top:72px;display:flex;gap:14px;font-size:7px}
.days span::before{content:"";display:inline-block;width:6px;height:6px;border:1px solid #555;margin-right:2px;vertical-align:-1px}
.card-back .note{position:absolute;left:0;right:0;top:148px;text-align:center;font-family:"Tinos",Georgia,serif;font-style:italic;font-size:7px;color:#fff;white-space:nowrap}
</style>
</head>
<body>

<!-- Letterhead -->
<section class="sheet letterhead">
  <div class="brand" style="left:45px;top:58px;--d:26px"><span class="brand-dot"></span><span class="brand-name" style="font-size:25px">Marlow Dental</span></div>
  <div class="tagline" style="left:98px;top:83px">Cosmetic, Emergency and Implant Restoration</div>
  <div class="corp" style="right:44px;top:84px">A Professional Dental Corporation</div>
  <div class="recipient">Your Street Address<br>Your City, State Zip<br>Date</div>
  <div class="body">
    <p>Lorem ipsum dolor sit amet, cu augue evertitur definitiones per, eum impetus tamquam dissentiet in. Enim sensibus ullamcorper mel ei, sit accumsan dissentias ad, usu cu fugit melius prodesset. Ea mei ancillae mandamus salutatus. Has ad sumo prima, eam in illum dissentiet, no sale graeci pro. Noster iuvaret moderatius no per.</p>
    <p>Movet soluta semper has te, graece cetero intellegat usu id. Everti meliore et vel, cu mea idque utroque nostrum. Cu ius lorem constituam, alii debet percipit vix at. Modus altera sea ei, vix dico constituto te. Cu eam nibh putent, est soluta reformidans eu. Esse nominavi vim ad, ne populo evertitur conceptam per.</p>
    <p>Usu zril facilisis laboramus eu, pro harum ancillae scripserit ad, pro in zril vocibus graecis. Duo id elit vocent, id nobis aperiam luptatum per. Est illum mediocrem reprehendunt ea, ius ut novum mazim deleniti. Et eos possit temporibus, erroribus referrentur et est. Usu purto virtute consetetur ea, ne pri novum mazim prompta.</p>
    <p>Nisl natum dicta usu no, sea id vidit forensibus, nec an prompta periculis. Eam id veniam accusata. Nulla adolescens constituam an his. Dolore constituam ex sea. Te pri commodo feugait laboramus, qui petentium consectetuer ea, an duo falli ridens graeco. Mei verear nostrud discere ei, postea noluisse honestatis eam eu.</p>
    <p>Modus reque harum cu vix, te hinc malis suscipiantur qui. In mutat mnesarchum vim, vitae partem verterem ex his. Has ferri vivendo liberavisse cu, nec at partem omnium, qui ea sale necessitatibus. Id brute elitr nonumy mei. Platonem conceptam posidonium nec in, ne putant feugiat suscipiantur vix.</p>
    <p>Yours sincerely,</p>
  </div>
  <div class="signature" role="img" aria-label="Handwritten signature of the dentist"></div>
  <div class="signer">Gordon T Vallow DMD, FAIDS</div>
  <div class="band-line"></div>
  <div class="band">
    <span class="contact"><svg viewBox="0 0 10 10"><path d="M5 1 1 5h1.5v4h2V6.5h1V9h2V5H9z"/></svg>48610 Marlow Avenue Larkdale, CA 90712</span>
    <span class="contact"><svg viewBox="0 0 10 10"><circle cx="5" cy="5" r="4.5" fill="none" stroke="#39b0e0"/><path d="M3.5 3h1l.5 1.3-.6.5c.3.6.7 1 1.3 1.3l.5-.6L7.5 6v1c-2 .2-4.2-2-4-4z"/></svg>(562) 471-3095</span>
    <span class="contact"><svg viewBox="0 0 10 10"><rect x="1" y="2.5" width="8" height="5.5" fill="none" stroke="#39b0e0"/><path d="M1 2.5 5 6l4-3.5" fill="none" stroke="#39b0e0"/></svg>gvallow@gvdmd-example.net</span>
    <span class="contact"><svg viewBox="0 0 10 10"><circle cx="5" cy="5" r="4.5"/></svg>gordonvallowdmd-example.com</span>
  </div>
</section>

<!-- Envelope front -->
<section class="sheet env-front">
  <div class="brand" style="left:22px;top:22px;--d:22px"><span class="brand-dot"></span><span class="brand-name" style="font-size:21px">Marlow Dental</span></div>
  <div class="tagline" style="left:66px;top:43px">Cosmetic, Emergency and Implant Restoration</div>
  <div class="corp" style="right:25px;top:23px">A Professional Dental Corporation</div>
  <div class="sender">
    <div class="name">Gordon T Vallow DMD, FAIDS</div>
    <div class="rows">
      <div class="col">☏ &nbsp;(562) 471-3095<br>✉ &nbsp;gvallow@gvdmd-example.net</div>
      <div class="col">48610 Marlow Avenue<br>Larkdale, CA 90712</div>
    </div>
  </div>
  <div class="window"></div>
  <div class="band-line"></div>
  <div class="band"></div>
</section>

<!-- Envelope back -->
<section class="sheet env-back">
  <svg class="flap" viewBox="0 0 564 76" aria-hidden="true">
    <defs><linearGradient id="flapGrad" x1="0" y1="0" x2="0" y2="1"><stop offset="0" stop-color="#3db4e4"/><stop offset="1" stop-color="#1a78b8"/></linearGradient></defs>
    <path d="M0 0H564L552 64Q550 76 538 76H26Q14 76 12 64Z" fill="url(#flapGrad)"/>
    <circle cx="282" cy="36" r="20" fill="none" stroke="#fff" stroke-width="2.5"/>
  </svg>
  <div class="web">www.gordonvallowdmd-example.com</div>
</section>

<!-- Business card front -->
<section class="sheet card-front">
  <div class="brand" style="left:13px;top:18px;--d:20px"><span class="brand-dot"></span><span class="brand-name" style="font-size:19px">Marlow Dental</span></div>
  <div class="tagline" style="left:54px;top:40px">Cosmetic, Emergency and Implant Restoration</div>
  <div class="band-line"></div>
  <div class="band">
    <div class="addr">48610 Marlow Avenue<br>Larkdale, CA 90712</div>
    <div class="lines"><b>P:</b> (562) 471-3095<br><b>T:</b> gvallow@gvdmd-example.net<br><b>W:</b> gordonvallowdmd-example.com</div>
    <div class="who">Gordon T Vallow DMD, FAIDS</div>
  </div>
  <div class="notch"></div>
</section>

<!-- Business card back: appointment -->
<section class="sheet card-back">
  <div class="brand" style="left:70px;top:14px;--d:18px"><span class="brand-dot"></span><span class="brand-name" style="font-size:18px;color:#fff">Marlow Dental</span></div>
  <div class="tagline" style="left:106px;top:33px;color:#ccc">Cosmetic, Emergency and Implant Restoration</div>
  <div class="form">
    <div class="field" style="left:14px;top:14px">Name <i style="width:196px"></i></div>
    <div class="field" style="left:14px;top:44px">Date <i style="width:75px"></i></div>
    <div class="field" style="left:114px;top:44px">Time <i style="width:70px"></i> am/pm</div>
    <div class="days"><span>MON</span><span>TUE</span><span>WED</span><span>THU</span><span>FRI</span><span>SAT</span></div>
  </div>
  <div class="note">If you are unable to keep your appoinment please call the office 24hours in advance</div>
</section>

</body>
</html>
```